African homeware retailer needs a web page design

We need a web page design for a new homeware and accessories store based in Johannesburg, South Africa. Our store carries modern African inspired items from designers that support social development and poverty alleviation initiatives. We have a particular preference for outfits that are centred on the empowerment of women.

Our business celebrates the skill, design and product of African craft and the work of designers looking to take that forward in a socially beneficial way (creating employment, developing skills, supporting local crafts people etc). We aim to carry items and inspirations from all over the African continent.

We would like to see a design that communicates African beauty and elegance without the typical tribal references that are made in reference to African craft or art.

We would like the web page to be stylish, uncomplicated, modern, captivating and appealing to the discerning customer. A similar value proposition is that of http://www.lindqvartworks.example/.

This is an e-commerce website which must be attractive to both individual buyers and design professionals so the website needs to look professional.

Here are links to some websites we like:
http://www.corvanhomes.example/
http://www.tesmoly.example/

Our logo is attached to the brief.

Target Market(s)

Our target market is female, age 20-50. However should not alienate the design conscious male customer therefore

Industry/Entity Type

E-Commerce

Requirements
Must have
• - A featured product banner which includes a photograph and text. This should be easy to edit as we will be changing the featured product regularly
- An easily expendable products section with categories. Examples of categories could be cushions, bedding, crockery etc. Should be easy to add new categories as well as new product pictures
- Home/landing page should be uncluttered
- Should use the logo and should be easy to change the logo which we have in various colour combinations. We plan to change the logo colours depending on circumstance e.g. make it red and white around Valentines day (similar to the way Zentrix frequently changes the logo on their landing page)

```html
<!DOCTYPE html>
<html lang="en">
<head>
<meta charset="utf-8">
<title>Amani Home — Homeware &amp; Accessories</title>
<link rel="stylesheet" href="https://fonts.googleapis.com/css2?family=Questrial&family=Montserrat:wght@600;700&family=Arimo:wght@400;700&display=swap">
<style>
:root{
  --cream:#fbf6d6;
  --cream-veil:rgba(251,246,214,.86);
  --green:#3a9a3c;
  --green-soft:#4fae4c;
  --navy:#0b3049;
  --navy-deep:#052a40;
  --band:rgba(4,52,74,.93);
  --teal-text:#2c5a6b;
  --ink:#1f3a48;
  --white:#ffffff;
  --star:#e2a12a;
  --star-off:#9aa39a;
  --photo-warm-1:#8f7355;
  --photo-warm-2:#b59a78;
  --photo-warm-3:#5a3f2b;
}
*{box-sizing:border-box;margin:0;padding:0}
html,body{width:1200px;height:1196px;overflow:hidden}
body{position:relative;background:var(--cream);font-family:"Questrial",sans-serif;color:var(--ink)}
.abs{position:absolute}

/* header */
.site-header{left:0;top:0;width:1200px;height:104px;background:var(--cream)}
.brand{left:160px;top:20px;display:flex;align-items:center;gap:14px}
.brand-mark{width:60px;height:60px;background:var(--green);border-radius:50%}
.brand-name{font-family:"Montserrat",sans-serif;font-weight:700;font-size:30px;color:var(--green);letter-spacing:1px}
.search{left:583px;top:11px;width:195px;height:28px;border:2px solid var(--teal-text);background:var(--cream);display:flex;align-items:center;padding-left:8px;gap:10px;font-size:15px;color:var(--teal-text)}
.account{top:14px;font-size:15px;color:var(--teal-text)}
.account.register{left:806px}
.account.login{left:868px;border-left:1px solid #b9c4a8;padding-left:11px}
.social{top:0;width:30px;height:40px;background:var(--green-soft);clip-path:polygon(0 0,100% 0,100% 78%,50% 100%,0 78%)}
.main-nav{left:618px;top:68px;display:flex;align-items:center;gap:14px;font-size:16px;color:var(--teal-text);letter-spacing:.3px}
.main-nav .active{color:var(--green)}
.main-nav .sep{width:16px;height:16px}

/* photo backdrop */
.hero-photo{left:0;top:104px;width:1200px;height:804px;background:
  radial-gradient(ellipse at 62% 40%,#c7b08e 0%,transparent 45%),
  linear-gradient(180deg,var(--photo-warm-2) 0%,var(--photo-warm-1) 50%,var(--photo-warm-3) 100%)}
.promo{left:165px;top:190px;width:451px;height:97px;background:var(--navy)}
.promo-kicker{left:5px;top:5px;width:441px;height:37px;background:var(--green);color:var(--white);font-family:"Montserrat",sans-serif;font-weight:600;font-size:17px;letter-spacing:4px;text-align:center;line-height:37px}
.promo-title{left:0;top:44px;width:451px;text-align:center;color:var(--white);font-family:"Montserrat",sans-serif;font-weight:700;font-size:35px;letter-spacing:1px;line-height:48px}
.thumb{top:296px;height:108px;border:3px solid #c9c3b5}
.shop-now{left:463px;top:411px;width:151px;height:42px;background:var(--navy);display:flex;align-items:center;color:var(--white);font-size:17px}
.shop-now span{padding-left:14px;width:110px}
.shop-now .go{width:41px;height:42px;background:var(--green);display:flex;align-items:center;justify-content:center}
.slider-arrow{top:282px;width:26px;height:58px}

/* intro band */
.intro-band{left:0;top:532px;width:1200px;height:112px;background:var(--band)}
.band-brand{left:172px;top:30px;font-family:"Montserrat",sans-serif;font-weight:700;font-size:30px;letter-spacing:5px;color:var(--white)}
.band-brand small{display:block;font-size:15px;color:var(--green);letter-spacing:4px;text-align:center;margin-bottom:-6px}
.intro-copy{left:453px;top:34px;width:540px;font-size:16px;line-height:23px;color:var(--white)}

/* featured */
.featured{left:0;top:644px;width:1200px;height:222px;background:var(--cream-veil)}
.featured-title{left:0;top:18px;width:1176px;text-align:center;font-family:"Montserrat",sans-serif;font-weight:700;font-size:18px;letter-spacing:4px;color:var(--green)}
.view-all{left:922px;top:18px;width:99px;height:24px;background:var(--navy);color:var(--white);font-family:"Montserrat",sans-serif;font-weight:700;font-size:13px;text-align:center;line-height:24px;letter-spacing:.5px}
.product{top:56px;width:146px}
.product-shot{position:relative;width:128px;height:88px;border:2px solid #d8d2c2}
.product-tools{position:absolute;right:0;bottom:0;width:46px;height:16px;background:#f3f0e6;display:flex;justify-content:space-around;align-items:center;font-size:10px;color:var(--navy)}
.product-name{margin-top:10px;font-size:12.5px;color:var(--teal-text);white-space:nowrap}
.product-buy{margin-top:6px;display:flex;align-items:center;gap:6px}
.add-cart{width:74px;height:18px;background:var(--navy);color:#dfe6ea;font-family:"Arimo",sans-serif;font-size:8.5px;display:flex;align-items:center;justify-content:space-between;padding:0 4px}
.add-cart i{width:10px;height:8px;background:var(--green-soft);border-radius:0 0 3px 3px}
.stars{font-size:9px;color:var(--star);letter-spacing:-.5px}
.stars em{font-style:normal;color:var(--star-off)}

/* footer */
.site-footer{left:0;top:908px;width:1200px;height:288px;background:var(--navy-deep);color:var(--white);font-family:"Arimo",sans-serif}
.footer-heading{font-family:"Montserrat",sans-serif;font-weight:700;font-size:20px;letter-spacing:.5px}
.connect{left:161px;top:32px}
.connect ul{list-style:none;margin-top:24px;font-size:11.5px;line-height:25.5px}
.blog{left:343px;top:32px;width:380px}
.blog-post{margin-top:12px;font-size:10.5px;line-height:16px}
.blog-post b{display:block;font-size:10.5px}
.blog-post + .blog-post{margin-top:16px}
.newsletter{left:777px;top:29px;width:240px;height:32px;background:#0a3a55;display:flex;align-items:center;justify-content:space-between;padding-left:10px;font-size:12px}
.newsletter button{width:72px;height:26px;margin-right:4px;background:var(--green);color:var(--white);border:0;font-family:"Questrial",sans-serif;font-size:13px}
.footer-brand{left:805px;top:163px;width:212px;height:96px;background:var(--cream);display:flex;align-items:center;justify-content:center;gap:10px}
.footer-brand .brand-name{font-size:25px}
.copyright{left:160px;top:234px;font-size:11.5px}
</style>
</head>
<body>

<header class="site-header abs">
  <div class="brand abs"><span class="brand-mark"></span><span class="brand-name">AMANI HOME</span></div>
  <div class="search abs">
    <svg width="14" height="14" viewBox="0 0 14 14"><circle cx="5.5" cy="5.5" r="4" fill="none" stroke="#0b3049" stroke-width="2"/><line x1="8.5" y1="8.5" x2="13" y2="13" stroke="#0b3049" stroke-width="2.4"/></svg>
    Search
  </div>
  <a class="account register abs">Register</a>
  <a class="account login abs">Log In</a>
  <span class="social abs" style="left:960px"></span>
  <span class="social abs" style="left:993px"></span>
  <span class="social abs" style="left:1026px"></span>
  <nav class="main-nav abs">
    <span class="active">HOME</span>
    <svg class="sep" viewBox="0 0 16 16"><line x1="2" y1="15" x2="14" y2="1" stroke="#8fb88a" stroke-width="1.4"/><line x1="6" y1="15" x2="16" y2="3" stroke="#8fb88a" stroke-width="1.4"/></svg>
    <span>CATALOUGE</span>
    <svg class="sep" viewBox="0 0 16 16"><line x1="2" y1="15" x2="14" y2="1" stroke="#8fb88a" stroke-width="1.4"/><line x1="6" y1="15" x2="16" y2="3" stroke="#8fb88a" stroke-width="1.4"/></svg>
    <span>ABOUT US</span>
    <svg class="sep" viewBox="0 0 16 16"><line x1="2" y1="15" x2="14" y2="1" stroke="#8fb88a" stroke-width="1.4"/><line x1="6" y1="15" x2="16" y2="3" stroke="#8fb88a" stroke-width="1.4"/></svg>
    <span>PRODUCTS</span>
  </nav>
</header>

<div class="hero-photo abs" role="img" aria-label="Photograph of a silver sculpture of a woman with a headwrap and earrings, warm brown studio background"></div>

<section class="promo abs">
  <div class="promo-kicker abs">HOMEWARE &amp; ACCESSORIES</div>
  <div class="promo-title abs">COLLECTION 2014</div>
</section>
<div class="thumb abs" style="left:166px;width:108px;background:linear-gradient(135deg,#6a4a2c,#b08a4d)" role="img" aria-label="Gold leopard figurine"></div>
<div class="thumb abs" style="left:280px;width:107px;background:linear-gradient(180deg,#c23a6b 0%,#f2eef0 60%)" role="img" aria-label="Pink patterned lamp"></div>
<div class="thumb abs" style="left:394px;width:107px;background:linear-gradient(135deg,#e05a2a,#3a8a3a 50%,#e8c030)" role="img" aria-label="Striped woven cushion"></div>
<div class="thumb abs" style="left:508px;width:107px;background:linear-gradient(180deg,#e8e4dc,#c49a6c)" role="img" aria-label="Printed tote bag"></div>
<a class="shop-now abs"><span>SHOP NOW</span><span class="go"><svg width="22" height="22" viewBox="0 0 22 22"><polyline points="3,2 11,11 3,20" fill="none" stroke="#0b3049" stroke-width="2"/><polyline points="10,2 18,11 10,20" fill="none" stroke="#0b3049" stroke-width="2"/></svg></span></a>
<svg class="slider-arrow abs" style="left:54px" viewBox="0 0 26 58"><polyline points="23,2 3,29 23,56" fill="none" stroke="#fff" stroke-width="3"/></svg>
<svg class="slider-arrow abs" style="left:1132px" viewBox="0 0 26 58"><polyline points="3,2 23,29 3,56" fill="none" stroke="#fff" stroke-width="3"/></svg>

<section class="intro-band abs">
  <div class="band-brand abs"><small>AMANI</small>HOME</div>
  <p class="intro-copy abs">Lorem ipsum dolor sit amet, consectetuer adipiscing elit, sed diam nonummy nibh euismod tincidunt ut laoreet dolore magna aliquam.</p>
</section>

<section class="featured abs">
  <h2 class="featured-title abs">FEATURED COLLECTION</h2>
  <a class="view-all abs">VIEW ALL</a>

  <article class="product abs" style="left:162px">
    <div class="product-shot" role="img" aria-label="Bedroom with red bedding" style="background:linear-gradient(135deg,#8a5a3a,#c8243a 60%,#e8d0b0)"><span class="product-tools">♥ ◉</span></div>
    <div class="product-name">BED ROOM COLLECTION</div>
    <div class="product-buy"><span class="add-cart">Add To Cart<i></i></span><span class="stars">★★★★<em>★★</em></span></div>
  </article>
  <article class="product abs" style="left:311px">
    <div class="product-shot" role="img" aria-label="Beaded necklace on a bust" style="background:linear-gradient(180deg,#f5f2ea,#c9a070)"><span class="product-tools">♥ ◉</span></div>
    <div class="product-name">JEWLLERY COLLECTION</div>
    <div class="product-buy"><span class="add-cart">Add To Cart<i></i></span><span class="stars">★★★★<em>★★</em></span></div>
  </article>
  <article class="product abs" style="left:453px">
    <div class="product-shot" role="img" aria-label="Bright printed textiles" style="background:linear-gradient(135deg,#e0701a,#c8301a 50%,#2a6a8a)"><span class="product-tools">♥ ◉</span></div>
    <div class="product-name">JEWLLERY COLLECTION</div>
    <div class="product-buy"><span class="add-cart">Add To Cart<i></i></span><span class="stars">★★★★<em>★★</em></span></div>
  </article>
  <article class="product abs" style="left:600px">
    <div class="product-shot" role="img" aria-label="Patterned mirrors" style="background:linear-gradient(135deg,#2a2420,#e8e0d8 50%,#c87870)"><span class="product-tools">♥ ◉</span></div>
    <div class="product-name">MIRRORS COLLECTION</div>
    <div class="product-buy"><span class="add-cart">Add To Cart<i></i></span><span class="stars">★★★★<em>★★</em></span></div>
  </article>
  <article class="product abs" style="left:747px">
    <div class="product-shot" role="img" aria-label="Pendant necklace" style="background:linear-gradient(180deg,#faf8f4,#d8a060)"><span class="product-tools">♥ ◉</span></div>
    <div class="product-name">ANTIQUECOLLECTION</div>
    <div class="product-buy"><span class="add-cart">Add To Cart<i></i></span><span class="stars">★★★★<em>★★</em></span></div>
  </article>
  <article class="product abs" style="left:892px">
    <div class="product-shot" role="img" aria-label="Gold table setting" style="background:linear-gradient(135deg,#4a3420,#c89a40 55%,#6a4a2a)"><span class="product-tools">♥ ◉</span></div>
    <div class="product-name">FURNITURE COLLECTION</div>
    <div class="product-buy"><span class="add-cart">Add To Cart<i></i></span><span class="stars">★★★★<em>★★</em></span></div>
  </article>
</section>

<footer class="site-footer abs">
  <div class="connect abs">
    <h3 class="footer-heading">CONNECT</h3>
    <ul><li>HOME</li><li>OUR SERVICES</li><li>OUR PRODUCTS</li><li>SPECIAL OFFERS</li><li>CONTACT</li></ul>
  </div>
  <div class="blog abs">
    <h3 class="footer-heading">FROM OUR BLOG</h3>
    <div class="blog-post"><b>AUG 19, 2013</b>Your Website Can Be Advertised via Backlinks<br>Being a blogging webmaster is nice, but it can get lonely at times. It would be advisable, therefore...</div>
    <div class="blog-post"><b>AUG 16, 2013</b>Website Visibility and Backlinks<br>The reason we talk so often about backlinks is because backlinks are very important when it comes to...</div>
  </div>
  <form class="newsletter abs"><span>Email Address</span><button type="button">SIGN UP</button></form>
  <div class="footer-brand abs"><span class="brand-name">AMANI HOME</span></div>
  <p class="copyright abs">Copyright © 2014 Amani Home. Privacy Policy - Terms of Conditions. All Rights Reserved</p>
</footer>

</body>
</html>
```